Business Card Design Project

business cards to match the logo design reference 1970674
specific details to be provided asap - message to follow
hello - thank you for the logo design (reference 1970674) which we are very happy with. In terms of business cards you presented a couple of options ie blue front/white back and then the reverse. Can we start with the white front version but change the text details to black font?
Actual details are as follows;
Dorian Plimsoll
Managing Director
e dorianplimsoll@kestrowe.com.au
t +61 2 5550 1937
m +61 400 555 219
Suite 712, Level 7, 48 Thornbury Rd
Sydney, NSW 2000, Australia
www.kestrowe.com.au

```html
<!DOCTYPE html>
<html lang="en">
<head>
<meta charset="utf-8">
<title>Kestrowe Business Card</title>
<link rel="stylesheet" href="https://fonts.googleapis.com/css2?family=Open+Sans:wght@400;600;700&display=swap">
<style>
  :root {
    --backdrop: #e9eaec;
    --card: #ffffff;
    --card-shade: #f1f2f3;
    --brand-blue: #1e7fd0;
    --brand-blue-light: #3aa3e6;
    --mark-grey: #5b5c5e;
    --ink: #1a1a1a;
    --rule: #d9dadc;
  }
  * { box-sizing: border-box; margin: 0; padding: 0; }
  html, body { width: 1200px; height: 646px; overflow: hidden; }
  body {
    background: var(--backdrop);
    font-family: "Open Sans", Arial, sans-serif;
    position: relative;
  }
  .card {
    position: absolute;
    top: 173px;
    width: 520px;
    height: 300px;
    background: linear-gradient(135deg, var(--card) 40%, var(--card-shade));
    box-shadow: 0 6px 18px rgba(0,0,0,0.12);
    overflow: hidden;
  }
  .card--back { left: 50px; }
  .card--front { left: 630px; }

  /* Back: contact side */
  .brand-panel {
    position: absolute; left: 0; top: 0; width: 220px; height: 100%;
    display: flex; align-items: center; justify-content: center;
  }
  .divider {
    position: absolute; left: 220px; top: 28px; bottom: 28px;
    width: 1px; background: var(--rule);
  }
  .brand {
    display: flex; align-items: center; gap: 10px;
  }
  .brand__square { background: var(--brand-blue); flex: none; }
  .brand__name {
    color: var(--mark-grey); font-weight: 700; letter-spacing: 0.5px;
  }
  .brand--small .brand__square { width: 18px; height: 18px; }
  .brand--small .brand__name { font-size: 26px; }

  .contact { position: absolute; left: 245px; top: 34px; right: 20px; }
  .contact__name {
    color: var(--brand-blue); font-size: 26px; font-weight: 400;
    font-variant: small-caps; letter-spacing: 1px; line-height: 1.1;
  }
  .contact__title {
    color: var(--ink); font-size: 11px; font-weight: 700;
    letter-spacing: 0.6px; text-transform: uppercase; margin-top: 2px;
  }
  .contact__list { list-style: none; margin-top: 20px; }
  .contact__item {
    display: flex; align-items: flex-start; gap: 10px;
    color: var(--ink); font-size: 11px; line-height: 15px; margin-bottom: 8px;
  }
  .contact__icon {
    width: 15px; height: 15px; flex: none; background: var(--brand-blue);
    border-radius: 2px; display: flex; align-items: center; justify-content: center;
  }
  .contact__icon svg { width: 11px; height: 11px; }

  /* Front */
  .front-body {
    position: absolute; left: 0; right: 0; top: 0; bottom: 22px;
    display: flex; flex-direction: column; align-items: center; justify-content: center;
  }
  .brand--large .brand__square { width: 40px; height: 40px; }
  .brand--large .brand__name { font-size: 62px; line-height: 1; }
  .front-url {
    align-self: flex-end; margin-right: 62px; margin-top: 4px;
    color: var(--brand-blue); font-size: 12px; font-weight: 700; letter-spacing: 0.5px;
  }
  .front-band {
    position: absolute; left: 0; right: 0; bottom: 0; height: 22px;
    background: linear-gradient(90deg, var(--brand-blue) 0 85%, var(--brand-blue-light) 85%);
  }
</style>
</head>
<body>

<section class="card card--back" aria-label="Card back with contact details">
  <div class="brand-panel">
    <div class="brand brand--small">
      <span class="brand__square"></span>
      <span class="brand__name">Kestrowe</span>
    </div>
  </div>
  <div class="divider"></div>
  <div class="contact">
    <h1 class="contact__name">Dorian Plimsoll</h1>
    <p class="contact__title">Managing Director</p>
    <ul class="contact__list">
      <li class="contact__item">
        <span class="contact__icon"><svg viewBox="0 0 12 12"><path d="M3 1.5l1.6 2.4-1 1c.6 1.3 1.5 2.2 2.5 2.7l1-1L9.5 8 8.6 10C5 9.6 2.4 7 2 3.4z" fill="#fff"/></svg></span>
        +61 2 5550 1937
      </li>
      <li class="contact__item">
        <span class="contact__icon"><svg viewBox="0 0 12 12"><rect x="3.5" y="1" width="5" height="10" rx="1" fill="#fff"/><rect x="4.5" y="2.2" width="3" height="6" fill="#1e7fd0"/></svg></span>
        +61 400 555 219
      </li>
      <li class="contact__item">
        <span class="contact__icon"><svg viewBox="0 0 12 12"><rect x="1.5" y="3" width="9" height="6" fill="#fff"/><path d="M1.5 3l4.5 3.5L10.5 3" stroke="#1e7fd0" fill="none"/></svg></span>
        dorianplimsoll@kestrowe.com.au
      </li>
      <li class="contact__item">
        <span class="contact__icon"><svg viewBox="0 0 12 12"><circle cx="6" cy="6" r="4.3" stroke="#fff" fill="none"/><ellipse cx="6" cy="6" rx="1.8" ry="4.3" stroke="#fff" fill="none"/><path d="M1.7 6h8.6" stroke="#fff"/></svg></span>
        www.kestrowe.com.au
      </li>
      <li class="contact__item">
        <span class="contact__icon"><svg viewBox="0 0 12 12"><path d="M6 11S2.5 7 2.5 4.5a3.5 3.5 0 017 0C9.5 7 6 11 6 11z" fill="#fff"/><circle cx="6" cy="4.5" r="1.2" fill="#1e7fd0"/></svg></span>
        <span>Suite 712, Level 7, 48 Thornbury Rd<br>Sydney, NSW 2000, Australia</span>
      </li>
    </ul>
  </div>
</section>

<section class="card card--front" aria-label="Card front">
  <div class="front-body">
    <div class="brand brand--large">
      <span class="brand__square"></span>
      <span class="brand__name">Kestrowe</span>
    </div>
    <p class="front-url">WWW.KESTROWE.COM.AU</p>
  </div>
  <div class="front-band"></div>
</section>

</body>
</html>
```